Homepage web design

I need a homepage design that will be easy to build into a default Word Press theme. Basically, header, navigation, body with sidebar, and footer.

This website is for a small commercial real estate firm in the Washington DC, Maryland and Virginia market.

THIS IS NOT A HOUSING/RESIDENTIAL WEBSITE. PLEASE DO NOT ADD ANY PROPERTY SEARCH FUNCTIONALITY.

Target Market(s)

People looking for basic information about the team and services provided.

Industry/Entity Type

Real Estate

Requirements
Must have
• Professional look. Clean design.

```html
<!DOCTYPE html>
<html lang="en">
<head>
<meta charset="utf-8">
<title>MCRB – Metro Capital Realty Brokerage</title>
<link rel="stylesheet" href="https://fonts.googleapis.com/css2?family=PT+Sans:wght@400;700&family=PT+Sans+Narrow:wght@400;700&family=PT+Serif:wght@700&display=swap">
<style>
:root{
  --green:#0f8a4f;
  --green-dark:#0c6b3d;
  --text:#2b2b2b;
  --muted:#6b6b6b;
  --header-bg:#f5f5f5;
  --band-bg:#efefef;
  --bottom-bg:#ececec;
  --footer-bg:#d4d4d4;
  --dark-panel:rgba(35,35,35,.88);
  --blue:#0d6fc4;
  --lime:#6aa80c;
  --line:#cfcfcf;
}
*{box-sizing:border-box;margin:0;padding:0}
html,body{width:1124px;height:1200px;overflow:hidden}
body{font-family:"PT Sans",sans-serif;color:var(--text);background:#fff;position:relative}
.abs{position:absolute}

/* header */
.site-header{left:0;top:0;width:1124px;height:106px;background:var(--header-bg);border-bottom:1px solid #e2e2e2}
.brand{left:95px;top:30px}
.brand-name{font-family:"PT Sans",sans-serif;font-weight:700;font-size:44px;line-height:44px;color:var(--green);letter-spacing:1px}
.brand-sub{font-family:"PT Sans",sans-serif;font-weight:700;font-size:10px;color:var(--green);letter-spacing:.2px;margin-top:-2px}
.main-nav{right:94px;top:34px;display:flex;height:36px}
.main-nav a{font-family:"PT Sans Narrow",sans-serif;font-size:13.5px;color:#333;text-decoration:none;padding:0 15px;line-height:36px;border-left:1px solid #dcdcdc}
.main-nav a:first-child{border-left:0}
.main-nav a.active{color:var(--green)}

/* hero */
.hero{left:94px;top:107px;width:936px;height:344px;background:linear-gradient(100deg,#4d6a2e 0%,#7c9a4a 25%,#c9c2b8 55%,#e8e2dc 75%,#6f8a45 100%)}
.hero-panel{left:94px;top:177px;width:454px;height:204px;background:var(--dark-panel);padding:16px 14px}
.hero-panel h1{font-family:"PT Sans Narrow",sans-serif;font-weight:700;font-size:32px;color:#fff;line-height:1.1;margin-bottom:8px}
.hero-panel p{font-size:12.5px;line-height:18.7px;color:#f2f2f2}
.btn-learn{left:389px;top:325px;width:144px;height:37px;border-radius:3px;background:linear-gradient(#2d8fe0,#0a5fae);font-family:"PT Serif",serif;font-weight:700;font-size:15px;color:#fff;text-align:center;line-height:37px;box-shadow:0 1px 2px rgba(0,0,0,.4)}

/* content */
.content-band{left:0;top:451px;width:1124px;height:330px;background:var(--band-bg);border-bottom:1px solid #e0e0e0}
.welcome{left:96px;top:468px;width:603px}
.welcome h2{font-weight:400;font-size:23px;color:var(--green);margin-bottom:6px}
.welcome p{font-size:10.6px;line-height:22.5px;text-align:justify;color:#222}

.newsletter{left:740px;top:468px;width:290px;height:97px;background:linear-gradient(#f3f3f3,#d9d9d9);border:1px solid #cfcfcf}
.newsletter svg{position:absolute;left:14px;top:12px}
.newsletter h3{position:absolute;left:55px;top:9px;font-family:"PT Sans Narrow",sans-serif;font-weight:700;font-size:19px;color:#444}
.newsletter .lead{position:absolute;left:55px;top:31px;font-size:11px;color:#555}
.email-field{position:absolute;left:17px;top:54px;width:218px;height:27px;background:#fff;border:1px solid #c8c8c8;font-size:9px;color:#888;line-height:25px;padding-left:6px}
.email-go{position:absolute;left:235px;top:54px;width:36px;height:27px;background:#2e2e2e}
.email-go svg{position:absolute;left:13px;top:8px}

.promo{left:740px;top:572px;width:290px;height:178px;background:linear-gradient(135deg,#d8d6d2,#8a8f98 60%,#4d5968)}
.promo-cap{left:740px;top:673px;width:290px;height:77px;background:var(--dark-panel);text-align:center;color:#fff}
.promo-cap h4{font-weight:400;font-size:17px;margin-top:5px}
.promo-cap p{font-size:10.5px;margin-top:1px}
.pill{display:inline-block;background:var(--green-dark);color:#fff;font-size:8.5px;padding:0 12px;line-height:21px;margin-top:6px}

/* financing tools */
.tools{left:0;top:781px;width:1124px;height:160px;background:#fff}
.tools h2{position:absolute;left:0;width:862px;top:14px;text-align:center;font-weight:400;font-size:28px;color:var(--green)}
.tools .tag{position:absolute;left:0;width:862px;top:48px;text-align:center;font-size:20px;color:#444}
.tool{position:absolute;top:80px;width:150px;text-align:center;font-size:11px;color:#777}
.tool svg{display:block;margin:0 auto 8px}
.btn-start{left:798px;top:838px;width:144px;height:37px;border-radius:3px;background:linear-gradient(#8fd12a,var(--lime));border:1px solid #5a8f0a;font-family:"PT Serif",serif;font-weight:700;font-size:15px;color:#fff;text-align:center;line-height:35px}

/* bottom */
.bottom{left:0;top:941px;width:1124px;height:183px;background:var(--bottom-bg)}
.col-title{font-size:13px;color:#333}
.news{left:95px;top:966px;width:284px}
.news-item{border-bottom:1px dashed #bbb;padding:6px 0 3px;font-size:10px;line-height:12.5px}
.news-item .date{color:#666}
.news-item .title{color:var(--green)}
.view-more{font-size:10px;color:#777;text-align:right;letter-spacing:.6px;margin-top:6px}
.divider{top:958px;width:1px;height:153px;background:var(--line)}
.testi{left:417px;top:966px;width:283px}
.avatar{position:absolute;left:2px;top:26px;width:74px;height:72px;border:1px solid #bbb;background:linear-gradient(#a47a5c,#d9b79b 55%,#e9e4df)}
.testi blockquote{position:absolute;left:91px;top:24px;width:192px;font-size:11px;line-height:13.5px;color:#777;text-align:justify}
.testi cite{display:block;font-style:normal;color:var(--green);font-size:10px}
.testi .rule{position:absolute;left:0;top:114px;width:283px;border-top:1px dashed #bbb}
.testi .view-more{position:absolute;right:0;top:119px}
.help{left:743px;top:969px;width:287px;height:141px;background:linear-gradient(90deg,#6b6e73,#d9d6d2 55%,#f1ede8)}
.help-panel{left:743px;top:983px;width:170px;height:87px;background:var(--dark-panel);padding:6px 11px;color:#fff}
.help-panel h4{font-weight:400;font-size:16px}
.help-panel p{font-size:10.5px;line-height:13px}
.help-panel .pill{margin-top:5px;font-size:8.5px;padding:0 14px}

/* footer */
.site-footer{left:0;top:1124px;width:1124px;height:76px;background:var(--footer-bg);text-align:center;font-size:10.5px;color:#444}
.site-footer nav{margin-top:18px}
.site-footer nav + nav{margin-top:10px}
.site-footer a{color:#444;text-decoration:none;margin:0 14px}
</style>
</head>
<body>

<header class="site-header abs">
  <div class="brand abs">
    <div class="brand-name">MCRB</div>
    <div class="brand-sub">METRO CAPITAL REALTY BROKERAGE</div>
  </div>
  <nav class="main-nav abs">
    <a href="#">HOME</a><a href="#">ABOUT MCRB</a><a href="#" class="active">SERVICES</a><a href="#">OUR AGENTS</a><a href="#">NEWS</a><a href="#">TESTIMONIALS</a><a href="#">FINANCING TOOLS</a><a href="#">CONTACT US</a>
  </nav>
</header>

<div class="hero abs" role="img" aria-label="Broker in a suit standing in front of a commercial office building"></div>
<section class="hero-panel abs">
  <h1>MCRB team-oriented approach</h1>
  <p>Lorem ipsum dolor sit amet, consectetur adipiscing elit. Morbi vitae nibh consectetur, dapibus nulla sit amet, faucibus nisl. Duis tristique sapien elit, ut eleifend metus ultricies non. In accumsan ut risus ac volutpat. Nunc vel sem a dolor varius vehicula. Etiam porttitor vehicula lacus</p>
</section>
<div class="btn-learn abs">Learn More</div>

<div class="content-band abs"></div>
<main class="welcome abs">
  <h2>Welcome to MCRB - Metro Capital Realty Brokerage</h2>
  <p>Lorem ipsum dolor sit amet, consectetur adipiscing elit. Praesent ac sem vitae justo fringilla ullamcorper. Quisque erat augue, lobortis a dolor sit amet, tristique commodo risus. Vivamus suscipit erat id felis fringilla porttitor. Phasellus a odio sit amet erat pharetra imperdiet. Maecenas fringilla ornare quam quis ornare. Ut sollicitudin elit vel neque mollis, vel ullamcorper lorem suscipit. Vivamus eu luctus nisl.</p>
  <p>Lorem ipsum dolor sit amet, consectetur adipiscing elit. Praesent ac sem vitae justo fringilla ullamcorper. Quisque erat augue, lobortis a dolor sit amet, tristique commodo risus. Vivamus suscipit erat id felis fringilla porttitor. Phasellus a odio sit amet erat pharetra imperdiet. Maecenas fringilla ornare quam quis ornare. Ut sollicitudin elit vel neque mollis, vel ullamcorper lorem suscipit. Vivamus eu luctus nisl. Lorem ipsum dolor sit amet, consectetur adipiscing elit. Praesent ac sem vitae justo fringilla ullamcorper. Quisque erat augue, lobortis a dolor sit amet, tristique commodo risus. Vivamus suscipit erat id felis fringilla porttitor. Phasellus a odio sit amet erat pharetra imperdiet. Maecenas fringilla ornare quam quis ornare. Ut sollicitudin elit vel neque mollis, vel ullamcorper lorem suscipit. Vivamus eu luctus nisl.</p>
</main>

<aside class="newsletter abs">
  <svg width="30" height="24" viewBox="0 0 30 24"><path d="M2 8 L22 2 L28 16 L8 22 Z" fill="#3cb44a"/><path d="M2 8 L16 13 L22 2" fill="none" stroke="#1e7a2b" stroke-width="1.2"/></svg>
  <h3>SIGN UP FOR OUR NEWSLETTER</h3>
  <div class="lead">Get our latest news and articles</div>
  <div class="email-field">ENTER EMAIL HERE</div>
  <div class="email-go"><svg width="10" height="11" viewBox="0 0 10 11"><path d="M0 0 L10 5.5 L0 11 Z" fill="#fff"/></svg></div>
</aside>
<div class="promo abs" role="img" aria-label="Commercial brokers reviewing lease documents at a desk"></div>
<div class="promo-cap abs">
  <h4>Looking for Commercial Space?</h4>
  <p>Ask Our Commercial Brokers, a team you can trust</p>
  <span class="pill">CLICK HERE FOR THE ANSWERS</span>
</div>

<section class="tools abs">
  <h2>Financing Tools</h2>
  <div class="tag">Online calculators help you plan every commercial property deal</div>
  <div class="tool" style="left:222px">
    <svg width="40" height="44" viewBox="0 0 40 44"><text x="20" y="40" text-anchor="middle" font-family="PT Sans,sans-serif" font-weight="700" font-size="48" fill="#1f5fb5">$</text></svg>
    LOAN CALCULATOR
  </div>
  <div class="tool" style="left:363px">
    <svg width="46" height="44" viewBox="0 0 46 44"><path d="M3 2 V41 H44" fill="none" stroke="#222" stroke-width="2"/><rect x="7" y="20" width="7" height="21" fill="#f08a1c"/><rect x="16" y="12" width="7" height="29" fill="#f08a1c"/><rect x="25" y="24" width="7" height="17" fill="#f08a1c"/><rect x="34" y="30" width="7" height="11" fill="#f08a1c"/><path d="M6 16 L18 8 L28 22 L42 26" fill="none" stroke="#2d9c3a" stroke-width="2.5"/></svg>
    MARKET ANALYSIS
  </div>
  <div class="tool" style="left:505px">
    <svg width="34" height="44" viewBox="0 0 34 44"><rect x="2" y="1" width="30" height="42" rx="2" fill="#c9c9c9" stroke="#8a8a8a"/><rect x="6" y="5" width="22" height="7" fill="#e9f1d9"/><g fill="#777"><rect x="6" y="16" width="5" height="4"/><rect x="14" y="16" width="5" height="4"/><rect x="22" y="16" width="5" height="4"/><rect x="6" y="23" width="5" height="4"/><rect x="14" y="23" width="5" height="4"/><rect x="22" y="23" width="5" height="4"/><rect x="6" y="30" width="5" height="4"/><rect x="14" y="30" width="5" height="4"/><rect x="22" y="30" width="5" height="4"/><rect x="6" y="37" width="13" height="3"/></g></svg>
    PROPERTY TAX CALCULATOR
  </div>
</section>
<div class="btn-start abs">Get Started</div>

<div class="bottom abs"></div>
<section class="news abs">
  <div class="col-title">LATEST NEWS</div>
  <div class="news-item"><div class="date">December 03, 2012</div><div class="title">Regional Commercial Leasing Forum</div></div>
  <div class="news-item"><div class="date">December 03, 2012</div><div class="title">Regional Commercial Leasing Forum</div></div>
  <div class="news-item"><div class="date">December 03, 2012</div><div class="title">Regional Commercial Leasing Forum</div></div>
  <div class="view-more">view more</div>
</section>
<div class="divider abs" style="left:400px"></div>
<section class="testi abs">
  <div class="col-title">CLIENTS TESTIMONIALS</div>
  <div class="avatar" role="img" aria-label="Portrait photo of a client"></div>
  <blockquote>Lorem ipsum dolor sit amet, consectetur adipiscing elit. Praesent ac sem vitae justo fringilla ullamcorper.<cite>Elena Morrow</cite></blockquote>
  <div class="rule"></div>
  <div class="view-more">view more</div>
</section>
<div class="divider abs" style="left:722px"></div>
<div class="help abs" role="img" aria-label="Smiling commercial broker giving a thumbs up"></div>
<div class="help-panel abs">
  <h4>NEED A HELP?</h4>
  <p>Find a Commercial Broker to help you today!</p>
  <span class="pill">CLICK HERE TO FIND AN AGENT</span>
</div>

<footer class="site-footer abs">
  <nav><a href="#">Home</a><a href="#">About MCRB</a><a href="#">Services</a><a href="#">Our Agents</a><a href="#">News</a><a href="#">Testimonials</a><a href="#">Financing Tools</a><a href="#">Contact Us</a></nav>
  <nav><a href="#">Terms &amp; Conditions</a><a href="#">Refund Policy</a><a href="#">Privacy Policy</a><a href="#">Site Map</a></nav>
</footer>

</body>
</html>
```